Certificate of Completion - Educational Trainings

We are looking for a certificate of completion for individuals who complete one of our specific trainings. Files should be provided in a Word (docx) or PowerPoint (pptx) format. The "Talmoray example.png" file is to show necessary information. Copies of logos have been included for design purposes.

Target Market(s)

Training Participants

Industry/Entity Type

Healthcare

Font styles to use
Sans Serif

```html
<!DOCTYPE html>
<html lang="en">
<head>
<meta charset="UTF-8">
<title>Talmoray Certificate of Completion</title>
<link rel="stylesheet" href="https://fonts.googleapis.com/css2?family=Montserrat:wght@800&family=Questrial&family=Josefin+Sans:wght@400&family=Great+Vibes&family=Allura&family=Mrs+Saint+Delafield&family=Sacramento&family=Oswald:wght@300&display=swap">
<style>
  :root {
    --frame-green: #6aae50;
    --ornament-green: #cfe6c3;
    --rule-green: #8cc474;
    --ink: #111111;
    --paper: #ffffff;
  }
  * { margin: 0; padding: 0; box-sizing: border-box; }
  html, body { width: 1200px; height: 855px; overflow: hidden; background: var(--paper); }
  .certificate {
    position: relative;
    width: 1200px;
    height: 855px;
    background: var(--frame-green);
    color: var(--ink);
  }
  .certificate__sheet {
    position: absolute;
    inset: 29px;
    background: var(--paper);
  }
  .certificate__ornament-band {
    position: absolute;
    inset: 33px;
    background: linear-gradient(135deg, #d6eacb, #c4e0b5 50%, #d6eacb);
  }
  .certificate__panel {
    position: absolute;
    inset: 70px;
    background: var(--paper);
    outline: 1.5px solid var(--rule-green);
    outline-offset: 2px;
  }
  .block { position: absolute; left: 0; width: 1200px; text-align: center; }

  .brand {
    top: 96px;
    display: flex;
    justify-content: center;
    align-items: center;
    gap: 18px;
  }
  .brand__dot {
    width: 52px; height: 52px; border-radius: 50%;
    background: var(--frame-green);
  }
  .brand__name {
    font-family: "Montserrat", sans-serif;
    font-weight: 800;
    font-size: 58px;
    letter-spacing: 3px;
    line-height: 1;
    color: var(--ink);
  }
  .sponsor-details {
    top: 156px;
    font-family: "Questrial", sans-serif;
    font-size: 14px;
    letter-spacing: 1.5px;
    line-height: 23px;
  }
  .title {
    top: 228px;
    font-family: "Questrial", sans-serif;
    font-size: 78px;
    letter-spacing: 5px;
    line-height: 1;
  }
  .subtitle {
    top: 312px;
    font-family: "Great Vibes", cursive;
    font-size: 50px;
    line-height: 1;
  }
  .awarded-to {
    top: 398px;
    font-family: "Questrial", sans-serif;
    font-size: 28px;
    letter-spacing: 2.5px;
    line-height: 1;
  }
  .recipient {
    top: 432px;
    font-family: "Allura", cursive;
    font-size: 48px;
    line-height: 1;
  }
  .recipient-rule {
    position: absolute; top: 493px; left: 389px; width: 366px;
    border-top: 1px solid var(--ink);
  }
  .course-details {
    top: 503px;
    font-family: "Josefin Sans", sans-serif;
    font-variant: small-caps;
    font-size: 23px;
    letter-spacing: 2.5px;
    line-height: 24px;
  }
  .sign-field { position: absolute; width: 287px; text-align: center; }
  .sign-field--date { left: 144px; top: 668px; }
  .sign-field--consultant { left: 696px; top: 652px; }
  .sign-field__value { height: 40px; line-height: 40px; }
  .sign-field--date .sign-field__value {
    font-family: "Sacramento", cursive; font-size: 28px; letter-spacing: 1px;
  }
  .sign-field--consultant .sign-field__value {
    font-family: "Mrs Saint Delafield", cursive; font-size: 38px; height: 54px; line-height: 54px;
  }
  .sign-field__rule { border-top: 1px solid var(--ink); }
  .sign-field__label {
    margin-top: 8px;
    font-family: "Questrial", sans-serif;
    font-size: 21px;
    letter-spacing: 2.5px;
    line-height: 1;
  }
  .seal {
    position: absolute; left: 530px; top: 668px; width: 140px;
    display: flex; flex-direction: column; align-items: center; gap: 8px;
  }
  .seal__dot { width: 46px; height: 46px; border-radius: 50%; background: var(--frame-green); }
  .seal__name {
    font-family: "Montserrat", sans-serif; font-weight: 800; font-size: 18px; letter-spacing: 1.5px;
  }
  .footnote {
    top: 762px;
    font-family: "Oswald", sans-serif;
    font-weight: 300;
    font-size: 13.5px;
    letter-spacing: 0.2px;
    line-height: 1;
    color: var(--ink);
  }
</style>
</head>
<body>
<main class="certificate">
  <div class="certificate__sheet"></div>
  <div class="certificate__ornament-band" role="img" aria-label="Decorative light green guilloche border pattern"></div>
  <div class="certificate__panel"></div>

  <header class="block brand">
    <span class="brand__dot"></span>
    <span class="brand__name">TALMORAY</span>
  </header>

  <p class="block sponsor-details">
    48 HARBOR LANE, STE. 302<br>
    BROOKHAVEN, ME 04219<br>
    NATIONAL REGISTRY SPONSOR NUMBER 71382
  </p>

  <h1 class="block title">CERTIFICATE</h1>
  <p class="block subtitle">of completion</p>

  <p class="block awarded-to">THIS CERTIFICATE IS AWARDED TO</p>
  <p class="block recipient">Marcus Ellingford</p>
  <div class="recipient-rule"></div>

  <p class="block course-details">
    For Successful completion of<br>
    Best Practices : Budget Process/Budget Building<br>
    Completed Online<br>
    Field of Study Finance<br>
    CPE Credits: 1
  </p>

  <div class="sign-field sign-field--date">
    <p class="sign-field__value">05/16/2024</p>
    <div class="sign-field__rule"></div>
    <p class="sign-field__label">COMPLETION DATE</p>
  </div>

  <div class="seal">
    <span class="seal__dot"></span>
    <span class="seal__name">TALMORAY</span>
  </div>

  <div class="sign-field sign-field--consultant">
    <p class="sign-field__value">Clara Wendell</p>
    <div class="sign-field__rule"></div>
    <p class="sign-field__label">SENIOR CONSULTANT</p>
  </div>

  <p class="block footnote">IN ACCORDANCE WITH THE STANDARD OF THE NATIONAL REGISTRY OF CPE SPONSORS CPE CREDITS HAVE BEEN GRANTED BASED ON A 50 MINUTE HOUR</p>
</main>
</body>
</html>
```